Travel Website Design

My client is a startup that will sell luxury hunting and fishing trips.
We do not have a logo as of yet, but I have attached 3 options for you to use in the mockup process. Please feel free to use any one (or all 3) of them, but don't base design around them.

Also attached is client's loose idea of how he wants an interior page to look. For the homepage, it would definitely need a rotating image slider, a search, and a tabbed section. The bluecranereelcasting.com is probably closest to what he is looking for.

Here are a few websites to pass along. In addition to the logos I have attached some links of company websites that are competition and have similar designs and layouts similar to what I am looking for.

http://www.bluecranereelcasting.com - The most direct competition that I have. I really like how they layout the pages and lodges info.

Tarvo.com - Close competition. Not a huge fan of how they search for lodges but like how they display each lodge and provide info.

http://www.qirandel.com/ - Example of a company website and layout the client does not like.

http://stonebrookjourneys.com/ - Clean feel. Not a fan of how they layout each lodges info.

```html
<!DOCTYPE html>
<html lang="en">
<head>
<meta charset="utf-8">
<title>Timber &amp; Tide – Luxury Hunting &amp; Fishing Trips</title>
<link rel="stylesheet" href="https://fonts.googleapis.com/css2?family=Oswald:wght@400;500;600&family=Open+Sans:wght@400;600;700&display=swap">
<style>
  :root {
    --forest-deep: #1c2616;
    --forest: #2f3d22;
    --moss: #6b8a2a;
    --leaf: #8db631;
    --lime: #a8cc3c;
    --sun: #f2d21b;
    --slate: #3a3d3a;
    --panel: #4a4d48;
    --ink: #1a1a1a;
    --paper: #ffffff;
    --mist: #c9cfc2;
  }
  * { margin: 0; padding: 0; box-sizing: border-box; }
  html, body { width: 828px; height: 1200px; overflow: hidden; }
  body {
    position: relative;
    font-family: "Open Sans", Arial, sans-serif;
    color: var(--paper);
    background:
      radial-gradient(ellipse at 50% 15%, #4f6136 0%, transparent 60%),
      linear-gradient(180deg, #3e4e2c 0%, var(--forest) 35%, var(--forest-deep) 75%, #121810 100%);
  }
  .abs { position: absolute; }

  /* header */
  .brand { left: 86px; top: 14px; display: flex; align-items: center; gap: 10px; }
  .brand-dot { width: 40px; height: 40px; border-radius: 50%; background: var(--leaf); }
  .brand-name { font-family: "Oswald", sans-serif; font-weight: 600; font-size: 30px; color: var(--paper); letter-spacing: .5px; }

  .contact-strip { right: 83px; top: 12px; display: flex; gap: 6px; font-size: 10px; font-weight: 600; }
  .contact-strip span { padding: 3px 7px; border: 1px solid var(--sun); color: var(--paper); }
  .contact-strip .hl { background: var(--sun); color: var(--ink); }

  .main-nav { left: 388px; top: 38px; width: 357px; height: 22px; background: var(--paper);
    display: flex; justify-content: space-around; align-items: center; font-size: 10px; color: var(--ink); font-weight: 600; }

  /* hero */
  .hero { left: 84px; top: 92px; width: 661px; height: 413px;
    background: linear-gradient(160deg, #5c7448 0%, #3d5a4a 40%, #6e8d8c 65%, #445542 100%); }
  .hero-title { left: 190px; top: 165px; width: 290px; text-align: center;
    font-family: "Oswald", sans-serif; font-weight: 600; font-size: 29px; line-height: 34px; color: var(--paper); }
  .hero-btn { left: 295px; top: 263px; width: 80px; height: 22px; background: var(--sun); color: var(--ink);
    font-size: 9px; font-weight: 700; display: flex; align-items: center; justify-content: center; }
  .hero-dots { left: 320px; top: 395px; display: flex; gap: 6px; }
  .hero-dots i { width: 7px; height: 7px; border-radius: 50%; background: var(--mist); display: block; }
  .hero-dots i.on { background: var(--sun); }

  .social { left: 747px; top: 150px; display: flex; flex-direction: column; gap: 4px; }
  .social i { display: block; width: 22px; height: 22px; background: var(--moss); }

  .intro { left: 86px; top: 516px; width: 658px; font-size: 10.5px; line-height: 15px; color: var(--mist); }

  /* deals + tabs */
  .deals-photo { left: 84px; top: 578px; width: 528px; height: 170px;
    background: linear-gradient(135deg, #5a6b3a 0%, #7b6a4a 45%, #3f4a2c 100%); }
  .deals-title { left: 106px; top: 690px; font-family: "Oswald", sans-serif; font-weight: 600; font-size: 30px; color: var(--paper); }
  .tabs { left: 84px; top: 748px; width: 528px; height: 34px; display: flex; background: var(--slate); }
  .tab { flex: 1; display: flex; align-items: center; justify-content: center; font-family: "Oswald", sans-serif;
    font-size: 12px; color: var(--paper); border-right: 1px solid #555; }
  .tab.active { background: var(--leaf); color: var(--ink); }
  .tab-body { left: 84px; top: 782px; width: 528px; height: 24px; background: var(--forest-deep); }

  .blog { left: 622px; top: 585px; width: 123px; height: 220px; background: var(--panel); padding: 10px 9px; }
  .blog h3 { font-family: "Oswald", sans-serif; font-weight: 400; font-size: 15px; margin-bottom: 8px; }
  .post { margin-bottom: 9px; }
  .post time { display: block; font-size: 7px; color: var(--mist); }
  .post h4 { font-size: 7.5px; color: var(--sun); font-weight: 600; margin: 2px 0; }
  .post p { font-size: 7px; line-height: 9.5px; color: var(--mist); }

  /* featured */
  .featured-bar { left: 84px; top: 820px; width: 661px; height: 36px; background: var(--leaf);
    display: flex; align-items: center; justify-content: center;
    font-family: "Oswald", sans-serif; font-weight: 500; font-size: 22px; color: var(--paper); }
  .featured-bar svg { position: absolute; left: 320px; top: 36px; }
  .cards { left: 84px; top: 878px; width: 661px; display: flex; gap: 9px; }
  .card { width: 158px; height: 170px; background: var(--slate); position: relative; }
  .card-photo { height: 82px; }
  .card h5 { font-size: 9.5px; font-weight: 600; margin: 8px 8px 4px; }
  .card p { font-size: 7.5px; line-height: 10px; color: var(--mist); margin: 0 8px; }
  .card .pin { position: absolute; left: 66px; bottom: -13px; width: 26px; height: 26px; border-radius: 50%;
    background: var(--forest-deep); border: 2px solid var(--leaf); display: flex; align-items: center; justify-content: center; }

  /* footer */
  .newsletter { left: 86px; top: 1090px; }
  .newsletter h6 { font-family: "Oswald", sans-serif; font-weight: 500; font-size: 12px; margin-bottom: 6px; }
  .newsletter-row { display: flex; }
  .newsletter-row span { width: 150px; height: 22px; background: var(--moss); font-size: 9px; padding: 5px 7px; color: var(--mist); }
  .go { width: 28px; height: 22px; background: var(--leaf); color: var(--ink); font-family: "Oswald", sans-serif; font-size: 12px;
    display: flex; align-items: center; justify-content: center; }
  .foot-contact { right: 83px; top: 1108px; display: flex; align-items: center; gap: 6px; font-size: 8.5px; font-weight: 600; white-space: nowrap; }
  .foot-contact b { font-family: "Oswald", sans-serif; font-weight: 500; font-size: 13px; margin-right: 4px; }
  .foot-contact span { padding: 4px 7px; background: var(--sun); color: var(--ink); border: 1px solid var(--sun); }
  .foot-contact span.plain { background: none; color: var(--paper); }
  .foot-bar { left: 84px; top: 1156px; width: 661px; height: 24px; background: #0e120b;
    display: flex; align-items: center; justify-content: space-between; padding: 0 10px; font-size: 8.5px; color: var(--mist); }
  .foot-bar nav { display: flex; gap: 16px; }
</style>
</head>
<body>

<header>
  <div class="abs brand"><span class="brand-dot"></span><span class="brand-name">Timber &amp; Tide</span></div>
  <div class="abs contact-strip">
    <span class="hl">888-555-0142</span>
    <span>INTL 01-1-406-555-0193</span>
    <span class="hl">info@timbertidetrips.com</span>
  </div>
  <nav class="abs main-nav">
    <span>Home</span><span>Conservation</span><span>Blog</span><span>Travel Tools</span><span>Become a Member</span><span>Contact Us</span>
  </nav>
</header>

<section>
  <div class="abs hero" role="img" aria-label="Angler on a river holding up a freshly caught trout"></div>
  <h1 class="abs hero-title">LOREM IPSUM DOL<br>DUIS AUTEM HENDRERI</h1>
  <a class="abs hero-btn">LEARN MORE</a>
  <div class="abs hero-dots"><i class="on"></i><i></i><i></i><i></i></div>
  <div class="abs social"><i></i><i></i><i></i><i></i></div>
</section>

<p class="abs intro">Lorem ipsum dolor sit amet, consectetuer adipiscing elit, sed diam nonummy nibh euismod tincidunt ut laoreet dolore magna aliquam erat volutpat. Ut wisi enim ad minim veniam, quis nostrud exerci tation ullamcorper suscipit lobortis nisl ut aliquip ex ea commodo consequat.</p>

<section>
  <div class="abs deals-photo" role="img" aria-label="Hunter's hands holding a rifle in autumn woods"></div>
  <h2 class="abs deals-title">SPECIAL DEALS:</h2>
  <div class="abs tabs">
    <div class="tab active">SPECIALS &amp; DEALS</div><div class="tab">TESTIMONIAL</div><div class="tab">SHOOTED TRIPS</div><div class="tab">COUPLES/FAMILY</div>
  </div>
  <div class="abs tab-body"></div>

  <aside class="abs blog">
    <h3>TRAVEL BLOG</h3>
    <div class="post"><time>Tuesday, June 10, 2014</time><h4>Lorem ipsum dolor sit amet elit</h4><p>Sed diam nonummy nibh euismod tincidunt ut laoreet dolore magna.</p></div>
    <div class="post"><time>Monday, June 9, 2014</time><h4>Duis autem vel eum iriure</h4><p>Ut wisi enim ad minim veniam quis nostrud exerci tation.</p></div>
    <div class="post"><time>Friday, June 6, 2014</time><h4>Nam liber tempor cum soluta</h4><p>Eleifend option congue nihil imperdiet doming id quod.</p></div>
  </aside>
</section>

<section>
  <h2 class="abs featured-bar">FEATURED TRIPS
    <svg width="20" height="10" viewBox="0 0 20 10"><path d="M0 0h20L10 10z" fill="#8db631"/></svg>
  </h2>
  <div class="abs cards">
    <article class="card">
      <div class="card-photo" role="img" aria-label="Two anglers on a riverbank" style="background:linear-gradient(135deg,#8fa4b0,#4e6450)"></div>
      <h5>Dolor Sitamet Neaum</h5><p>Lorem ipsum dolor sit amet, consectetuer adipiscing elit sed diam nonummy.</p>
      <span class="pin"><svg width="10" height="14" viewBox="0 0 10 14"><path d="M5 0a5 5 0 0 1 5 5c0 4-5 9-5 9S0 9 0 5a5 5 0 0 1 5-5z" fill="#8db631"/><circle cx="5" cy="5" r="2" fill="#1c2616"/></svg></span>
    </article>
    <article class="card">
      <div class="card-photo" role="img" aria-label="Lake and mountains at sunset" style="background:linear-gradient(135deg,#6a7fa0,#c08a4a)"></div>
      <h5>Dolor Sitamet Neaum</h5><p>Lorem ipsum dolor sit amet, consectetuer adipiscing elit sed diam nonummy.</p>
      <span class="pin"><svg width="10" height="14" viewBox="0 0 10 14"><path d="M5 0a5 5 0 0 1 5 5c0 4-5 9-5 9S0 9 0 5a5 5 0 0 1 5-5z" fill="#8db631"/><circle cx="5" cy="5" r="2" fill="#1c2616"/></svg></span>
    </article>
    <article class="card">
      <div class="card-photo" role="img" aria-label="Fly fisherman casting in open water" style="background:linear-gradient(135deg,#4f7c93,#2e4a3a)"></div>
      <h5>Dolor Sitamet Neaum</h5><p>Lorem ipsum dolor sit amet, consectetuer adipiscing elit sed diam nonummy.</p>
      <span class="pin"><svg width="10" height="14" viewBox="0 0 10 14"><path d="M5 0a5 5 0 0 1 5 5c0 4-5 9-5 9S0 9 0 5a5 5 0 0 1 5-5z" fill="#8db631"/><circle cx="5" cy="5" r="2" fill="#1c2616"/></svg></span>
    </article>
    <article class="card">
      <div class="card-photo" role="img" aria-label="Couple on a boat showing their catch" style="background:linear-gradient(135deg,#7aa3c0,#6f5a48)"></div>
      <h5>Dolor Sitamet Neaum</h5><p>Lorem ipsum dolor sit amet, consectetuer adipiscing elit sed diam nonummy.</p>
      <span class="pin"><svg width="10" height="14" viewBox="0 0 10 14"><path d="M5 0a5 5 0 0 1 5 5c0 4-5 9-5 9S0 9 0 5a5 5 0 0 1 5-5z" fill="#8db631"/><circle cx="5" cy="5" r="2" fill="#1c2616"/></svg></span>
    </article>
  </div>
</section>

<footer>
  <div class="abs newsletter">
    <h6>GET OUR E NEWSLETTER</h6>
    <div class="newsletter-row"><span>Email Address</span><div class="go">GO</div></div>
  </div>
  <div class="abs foot-contact">
    <b>CONTACT</b>
    <span>888-555-0142</span>
    <span class="plain">INTL 01-1-406-555-0193</span>
    <span>info@timbertidetrips.com</span>
  </div>
  <div class="abs foot-bar">
    <nav><span>Home</span><span>Conservation</span><span>Blog</span><span>Travel Tools</span><span>Become a Member</span><span>Contact Us</span></nav>
    <span>© 2014 Timber &amp; Tide. All Rights Reserved.</span>
  </div>
</footer>

</body>
</html>
```